Home page in PSD needed for a Business Consultant website

We have been given the mandate to re-do the website: http://www.lumivanconseil.ca/

Deliverable: home page in PSD format in French language

Context: Luc Dorval is a business strategist specializing in marketing, creativity, business development. He helps small and medium companies develop their business through creative marketing strategies.

Some websites we like for your inspiration:

http://www.tallpinegrove.com.au/
http://www.trwadvisory.com.au/
http://fjalladvisors.com.au/
http://www.olubrenix.com/fr

Target Market(s)

B2B: Companies looking on the web for a business consultant who can help them with marketing, business developement, printing needs.

Industry/Entity Type

Business

Requirements
Must have
• Call to action: "Simplifiez votre développement des affaires" (which means "Simplify your business development")
• List of services (main menu)
• Marketing
• Développement des affaires
• Créativité
• Scolaire
• Impression
• Top menu as follow:
• Accueil
• À propos
• Contact

```html
<!DOCTYPE html>
<html lang="fr">
<head>
<meta charset="utf-8">
<title>Lumivan Conseil — Accueil</title>
<link rel="stylesheet" href="https://fonts.googleapis.com/css2?family=Lobster&family=Source+Sans+3:wght@300;400;600;700&display=swap">
<style>
  :root {
    --white: #ffffff;
    --ink: #111111;
    --grey-text: #6b6b6b;
    --grey-title: #505050;
    --circle-grey: #e9e9e9;
    --circle-ring: #dcdcdc;
    --icon-dark: #2b2b2b;
    --brand-blue: #0a6fc2;
    --navy: #0b3a8f;
    --navy-ring: #072e78;
    --link-blue: #0c3d97;
    --accent-orange: #ff4a12;
    --button-top: #f0420d;
    --button-bottom: #a81b04;
    --hero-deep: #0a4aa8;
    --hero-mid: #1778d0;
    --hero-light: #3ab4ec;
    --footer: #000000;
    --social: #ffffff;
  }
  * { margin: 0; padding: 0; box-sizing: border-box; }
  html, body { width: 1200px; height: 1182px; overflow: hidden; background: var(--white); }
  body { font-family: "Source Sans 3", "Myriad Pro", sans-serif; color: var(--ink); position: relative; }
  a { color: inherit; text-decoration: none; }

  .site-header { position: absolute; left: 0; top: 0; width: 1200px; height: 93px; }
  .brand { position: absolute; left: 134px; top: 30px; display: flex; align-items: center; gap: 10px; }
  .brand-mark { width: 30px; height: 30px; border-radius: 50%; background: var(--brand-blue); }
  .brand-name { font-size: 26px; font-weight: 400; color: var(--icon-dark); letter-spacing: .3px; }
  .top-menu { position: absolute; left: 560px; top: 37px; display: flex; gap: 22px; font-size: 15px; font-weight: 600; color: var(--grey-title); }
  .contact-card { position: absolute; left: 970px; top: 31px; line-height: 22px; font-size: 18px; font-weight: 600; }
  .contact-name { color: var(--brand-blue); }
  .contact-phone { color: var(--accent-orange); }

  .hero {
    position: absolute; left: 0; top: 93px; width: 1200px; height: 494px;
    background:
      radial-gradient(ellipse 520px 300px at 640px 260px, rgba(120,210,250,.55), transparent 70%),
      linear-gradient(160deg, var(--hero-deep) 0%, var(--hero-mid) 45%, var(--hero-light) 75%, var(--hero-mid) 100%);
  }
  .hero-title {
    position: absolute; left: 134px; top: 52px; width: 660px; white-space: nowrap;
    font-family: "Lobster", cursive; font-weight: 400; font-size: 47px; line-height: 58px;
    color: var(--white); text-shadow: 0 2px 3px rgba(0,0,0,.25);
  }
  .hero-lead {
    position: absolute; left: 136px; top: 240px; width: 640px; white-space: nowrap;
    font-size: 22px; line-height: 28px; font-weight: 400; color: var(--white);
  }
  .cta {
    position: absolute; left: 135px; top: 356px; height: 60px;
    border: 3px solid #1a5fd0; border-radius: 6px;
    background: linear-gradient(var(--button-top), var(--button-bottom));
    display: flex; align-items: center; gap: 12px; padding: 0 20px 0 19px;
    color: var(--white); font-size: 16.5px; font-weight: 600; letter-spacing: .2px; white-space: nowrap;
  }
  .slider-dots {
    position: absolute; left: 551px; top: 466px; width: 99px; height: 28px;
    background: var(--white); border-radius: 3px 3px 0 0;
    display: flex; justify-content: center; align-items: center; gap: 4px;
  }
  .slider-dots span { width: 9px; height: 9px; border-radius: 50%; background: #d9d9d9; }
  .slider-dots span.active { background: #3b7fd6; }

  .portrait {
    position: absolute; left: 836px; top: 9px; width: 124px; height: 636px;
    border-radius: 50px 50px 16px 16px;
    background: linear-gradient(#2a2d3a 0%, #1f222c 60%, #15171d 100%);
    opacity: .92;
  }

  .services-intro { position: absolute; left: 0; top: 647px; width: 1200px; text-align: center; }
  .services-heading { font-size: 28px; line-height: 36px; font-weight: 300; color: var(--ink); }
  .services-heading strong { font-weight: 600; }
  .services-sub { margin-top: 10px; font-size: 16.5px; font-weight: 300; color: var(--grey-text); }

  .service { position: absolute; top: 739px; width: 320px; text-align: center; }
  .service-icon {
    width: 143px; height: 143px; border-radius: 50%; margin: 0 auto;
    background: var(--circle-grey); border: 8px solid var(--circle-ring);
    display: flex; align-items: center; justify-content: center;
  }
  .service-title { margin-top: 12px; font-size: 20px; font-weight: 400; color: var(--grey-title); }
  .service-list { list-style: none; margin-top: 6px; font-size: 13px; line-height: 18.5px; color: var(--grey-text); }
  .service--active .service-icon { background: var(--navy); border-color: var(--navy-ring); }
  .service--active .service-title, .service--active .service-list { color: var(--link-blue); }
  .service--1 { left: 129px; }
  .service--2 { left: 439px; }
  .service--3 { left: 750px; }

  .site-footer { position: absolute; left: 0; top: 1098px; width: 1200px; height: 84px; background: var(--footer); color: var(--white); }
  .footer-nav { position: absolute; left: 135px; top: 28px; display: flex; gap: 13px; font-size: 12.5px; font-weight: 600; }
  .footer-copy { position: absolute; left: 135px; top: 52px; font-size: 12px; font-weight: 600; }
  .social { position: absolute; left: 911px; top: 31px; display: flex; gap: 9px; }
  .social span { width: 32px; height: 32px; border-radius: 50%; background: var(--social); }
</style>
</head>
<body>
  <header class="site-header">
    <div class="brand"><span class="brand-mark"></span><span class="brand-name">Lumivan Conseil</span></div>
    <nav class="top-menu"><a>Accueil</a><a>À propos</a><a>Contact</a></nav>
    <div class="contact-card">
      <div class="contact-name">Luc Dorval</div>
      <div class="contact-phone">514 555 0182</div>
    </div>
  </header>

  <section class="hero">
    <h1 class="hero-title">Votre guichet unique pour vos<br>besoins en vente, marketing<br>et commercialisation!</h1>
    <p class="hero-lead">Luc Dorval, fin stratège, audacieux et créatif,<br>développe des concepts avant-gardistes provoquant,<br>chez les entreprises qu'il dessert, des ventes éminentes.</p>
    <a class="cta">
      <svg width="18" height="16" viewBox="0 0 18 16" aria-hidden="true"><rect x="0" y="6" width="4" height="10" fill="#fff"/><path d="M5 6 L9 0 C11 0 11 2 10.5 5 H16 C17.5 5 18 6 17.5 7.5 L15.5 15 C15 16 14.5 16 13.5 16 H5 Z" fill="#fff"/></svg>
      Simplifiez votre développement des affaires
    </a>
    <div class="slider-dots"><span></span><span class="active"></span><span></span><span></span><span></span></div>
  </section>

  <div class="portrait" role="img" aria-label="Photo en pied de Luc Dorval, souriant, en complet sombre"></div>

  <section class="services-intro">
    <h2 class="services-heading">Vous voulez savoir? <strong>Comment Luc Dorval peut vous aider...</strong></h2>
    <p class="services-sub">If you aliquam lorem ipsum dolor sit amet consectetur adipiscing elit duis. Sed ut parspatrisas ut dolore ante!</p>
  </section>

  <article class="service service--1">
    <div class="service-icon">
      <svg width="60" height="52" viewBox="0 0 60 52" aria-hidden="true"><circle cx="26" cy="13" r="12" fill="#2b2b2b"/><path d="M0 52 C2 32 14 26 26 26 C32 26 36 28 38 30 C32 34 30 42 30 52 Z" fill="#2b2b2b"/><circle cx="45" cy="31" r="7" fill="#2b2b2b"/><path d="M33 52 C33 43 38 39 45 39 C52 39 58 43 58 52 Z" fill="#2b2b2b"/></svg>
    </div>
    <h3 class="service-title">Commercialisation</h3>
    <ul class="service-list"><li>Outils de diffusion</li><li>Marketing Web</li><li>Graphisme</li><li>Rédaction</li><li>Communication</li></ul>
  </article>

  <article class="service service--2 service--active">
    <div class="service-icon">
      <svg width="48" height="48" viewBox="0 0 48 48" aria-hidden="true"><rect x="0" y="22" width="12" height="26" fill="#fff"/><rect x="18" y="0" width="12" height="48" fill="#fff"/><rect x="36" y="14" width="12" height="34" fill="#fff"/></svg>
    </div>
    <h3 class="service-title">Marketing</h3>
    <ul class="service-list"><li>Planification et organisation</li><li>Orientations stratégiques de commercialisation</li><li>Médias sociaux</li><li>Branding</li><li>Publicité</li></ul>
  </article>

  <article class="service service--3">
    <div class="service-icon">
      <svg width="46" height="54" viewBox="0 0 46 54" aria-hidden="true"><g stroke="#2b2b2b" stroke-width="3" stroke-linecap="round"><line x1="23" y1="1" x2="23" y2="8"/><line x1="11" y1="4" x2="14" y2="10"/><line x1="35" y1="4" x2="32" y2="10"/><line x1="2" y1="12" x2="8" y2="15"/><line x1="44" y1="12" x2="38" y2="15"/></g><path d="M23 13 C31 13 35 19 35 25 C35 32 29 35 28 42 H18 C17 35 11 32 11 25 C11 19 15 13 23 13 Z" fill="#2b2b2b"/><rect x="18" y="44" width="10" height="2.5" fill="#2b2b2b"/><rect x="18" y="48" width="10" height="2.5" fill="#2b2b2b"/><rect x="20" y="52" width="6" height="2" fill="#2b2b2b"/></svg>
    </div>
    <h3 class="service-title">Créativité</h3>
    <ul class="service-list"><li>Outils de diffusion</li><li>Marketing Web</li><li>Graphisme</li><li>Rédaction</li><li>Communication</li></ul>
  </article>

  <footer class="site-footer">
    <nav class="footer-nav"><a>Marketing</a><a>Développement des affaires</a><a>Créativité</a><a>Scolaire</a><a>Impression</a></nav>
    <p class="footer-copy">© Lumivan Conseil 2013. Tous droits réservés</p>
    <div class="social" aria-label="Réseaux sociaux"><span></span><span></span><span></span><span></span></div>
  </footer>
</body>
</html>
```